CREATE A BUSINESS CARD FOR A BOAT CLEANING SERVICE

WE ARE STARTING A NEW BOAT CLEANING BUSINESS. WE DIVE UNDERWATER TO CLEAN BOAT HULLS, JETTIES, UNDERWATER STRUCTURES ETC. WE ARE LOOKING FOR AN UPPERMARKET MODERN LOGO AND BUSINESS CARD AS ALOT OF OUR TARGET MARKET WILL BE HIGH END. YOU HAVE TO DESIGN A BUSINESS CARD AND LOGO SEPERATELY .
THE BUSINESS CARD DIMESNION MUST BE STANDARD SIZE.
The standard dimensions of a printed business card are 3.5 x 2 inches

Target Market(s)

UNDERWATER SERVICED

Industry/Entity Type

Business

Contact Information for Business Card

HALDANE SUBSEA SERVICES

Font styles to use
Serif

Colors

Designer to choose colors to be used in the design.

Requirements
Must have
• HALDANE
Nice to have
• dark
Should not have
• more than 3 colors

```html
<!DOCTYPE html>
<html lang="en">
<head>
<meta charset="utf-8">
<title>Haldane Subsea Services – Business Card</title>
<link href="https://fonts.googleapis.com/css2?family=Cinzel:wght@400&family=Open+Sans:wght@400;600&display=swap" rel="stylesheet">
<style>
  :root {
    --backdrop: #ece9e4;
    --card-grey: #717171;
    --card-white: #ffffff;
    --navy: #16508c;
    --sea-blue: #2e72bb;
    --ink-light: #ffffff;
  }
  html, body {
    margin: 0;
    padding: 0;
    width: 1200px;
    height: 900px;
    overflow: hidden;
    background: var(--backdrop);
  }
  .canvas {
    position: relative;
    width: 1200px;
    height: 900px;
  }
  .card {
    position: absolute;
    box-shadow: 0 6px 18px rgba(0,0,0,0.18);
    overflow: hidden;
  }
  .card--contact {
    left: 78px;
    top: 35px;
    width: 587px;
    height: 362px;
    background: var(--card-grey);
    color: var(--ink-light);
    font-family: "Open Sans", Arial, sans-serif;
  }
  .card--brand {
    left: 388px;
    top: 505px;
    width: 566px;
    height: 352px;
    background: var(--card-white);
  }
  .wave-art {
    position: absolute;
    right: 0;
    top: 0;
    width: 400px;
    height: 362px;
  }
  .holder {
    position: absolute;
    left: 30px;
    top: 44px;
  }
  .holder__name {
    margin: 0;
    font-size: 19px;
    font-weight: 600;
    letter-spacing: 0.2px;
    line-height: 1.1;
  }
  .holder__title {
    margin: 2px 0 0;
    font-size: 15px;
    font-weight: 400;
  }
  .contacts {
    position: absolute;
    left: 31px;
    top: 188px;
    margin: 0;
    padding: 0;
    list-style: none;
    font-size: 15px;
    line-height: 22px;
  }
  .contacts li {
    display: flex;
    align-items: center;
    gap: 7px;
  }
  .contacts svg {
    width: 11px;
    height: 11px;
    fill: var(--ink-light);
    flex: none;
  }
  .address {
    position: absolute;
    left: 31px;
    top: 271px;
    margin: 0;
    font-size: 15px;
    line-height: 22px;
    font-style: normal;
  }
  .wordmark {
    position: absolute;
    left: 0;
    right: 0;
    top: 186px;
    text-align: center;
    font-family: "Cinzel", Georgia, serif;
    font-weight: 400;
    color: var(--navy);
  }
  .wordmark__name {
    display: block;
    font-size: 58px;
    line-height: 1;
    letter-spacing: 2px;
    margin-left: 40px;
  }
  .wordmark__line {
    display: block;
    font-size: 19px;
    letter-spacing: 2.5px;
    margin-top: 6px;
    margin-left: 40px;
  }
</style>
</head>
<body>
<main class="canvas">

  <section class="card card--contact">
    <svg class="wave-art" viewBox="0 0 400 362" role="img" aria-label="Abstract blue and white hull-and-wave decoration">
      <defs>
        <linearGradient id="seaFade" x1="0" y1="0" x2="1" y2="0.2">
          <stop offset="0" stop-color="#717171" stop-opacity="0"/>
          <stop offset="0.55" stop-color="#16508c" stop-opacity="0.55"/>
          <stop offset="1" stop-color="#2e72bb" stop-opacity="0.85"/>
        </linearGradient>
      </defs>
      <rect width="400" height="362" fill="url(#seaFade)"/>
    </svg>

    <header class="holder">
      <h1 class="holder__name">MARCUS HALE</h1>
      <p class="holder__title">Managing Director</p>
    </header>

    <ul class="contacts">
      <li>
        <svg viewBox="0 0 24 24"><path d="M6.6 10.8a15.1 15.1 0 0 0 6.6 6.6l2.2-2.2c.3-.3.7-.4 1-.2 1.1.4 2.3.6 3.6.6.6 0 1 .4 1 1V20c0 .6-.4 1-1 1A17 17 0 0 1 3 4c0-.6.4-1 1-1h3.5c.6 0 1 .4 1 1 0 1.3.2 2.5.6 3.6.1.3 0 .7-.2 1z"/></svg>
        (044)987650321
      </li>
      <li>
        <svg viewBox="0 0 24 24"><path d="M2 5h20v14H2z M3 6l9 7 9-7" fill="#fff"/><path d="M3 6.5l9 6.5 9-6.5" stroke="#717171" stroke-width="1.6" fill="none"/></svg>
        info@haldanesubsea.com
      </li>
      <li>
        <svg viewBox="0 0 24 24"><circle cx="12" cy="12" r="10"/><path d="M12 2c-3 3-3 17 0 20M2 12h20" stroke="#717171" stroke-width="1.4" fill="none"/></svg>
        www.haldanesubsea.com
      </li>
    </ul>

    <address class="address">48 Harbour Quay, Portside,<br>Westland, 40210</address>
  </section>

  <section class="card card--brand">
    <p class="wordmark">
      <span class="wordmark__name">HALDANE</span>
      <span class="wordmark__line">SUBSEA SERVICES</span>
    </p>
  </section>

</main>
</body>
</html>
```